New KVL Identification sticker

Looking for a new look to the attached sticker. We want to keep the original in the design and would like to incorporate our vision statement and company history some way into the new design. Holograph overlay would be encouraged in the sticker design, You can also research more about the company through the website: http://www.lunbrextor.example/
Updates

Please remember in the designs you do not have to capture the all the verbiage within the mission or vision statement or the history. I want you to take the verbiage meaning or highlight the history within the design. Also the old design must be somewhere within the new design to keep the history. I do like some of what is being done but I do not see the story within the design as of yet. A few more things about the company: High quality Union Proud shop Employing hard working people Craftsmanship Years of service in the industry Hard work and dedication goes into every blade overhaul Go to the kestrel vane laboratories website and learn more about the company. It will be the message in the design and the feeling proud of the work that was done message that I think the CEO will be looking for. Keep it simple but bring make it modern. I know we can not capture everything in one sticker. But use something that will help draw people into the overhaul message that the work completed by KVL is the highest quality and it was done to the highest standard by experienced people that care about what they do. OK Thanks

Thank you everyone that has been submitting your designs. So many great ideals. Sorry I have not been getting back to everyone. I am reviewing all the designs and waiting for some feed back from the others involved in this project. It is going to take at least this week to get through the designs and to narrow down the selection. Because this is a group effort on my side it is not easy to get everyone together to get a fast decision so I apologies in advance for the length of time this is taking. I hope to be working with some of you soon to tweak the designs and for our group to pick the design we will be going with. Please be patient and we will be in touch soon. This is the first time we have used this service so we are learning as we go forward. Thank you again, I look forward to working with one of you soon. You all have been great. Be back to you all soon with more information as I get it.

Target Market(s)

Aircraft operators that fly aircraft with propellers

Colors

Designer to choose colors to be used in the design.

Requirements
Must have
• Incorporate our old design into the new one
Nice to have
• Hologram

```html
<!DOCTYPE html>
<html lang="en">
<head>
<meta charset="utf-8">
<title>KVL Identification Sticker</title>
<link rel="stylesheet" href="https://fonts.googleapis.com/css2?family=Oswald:wght@500;700&display=swap">
<style>
  :root {
    --page: #fdfdfd;
    --panel: #464241;
    --holo-blue: #8fd3ec;
    --holo-green: #a6d79a;
    --holo-violet: #7a74c2;
    --holo-pink: #f0a9c8;
    --holo-mint: #a6dcd3;
    --holo-yellow: #ece58a;
    --name-tone: #e6cfe3;
  }
  html, body {
    margin: 0;
    padding: 0;
    width: 1060px;
    height: 1200px;
    overflow: hidden;
    background: var(--page);
  }
  .sticker {
    display: block;
    width: 1060px;
    height: 1200px;
  }
  .tagline {
    font-family: "Oswald", sans-serif;
    font-weight: 500;
    font-size: 17px;
  }
  .company-name {
    font-family: "Oswald", sans-serif;
    font-weight: 700;
    fill: var(--name-tone);
  }
  .services {
    font-family: "Oswald", sans-serif;
    font-weight: 500;
    font-size: 18px;
  }
  .panel { fill: var(--panel); }
  .brand-circle { fill: var(--name-tone); }
</style>
</head>
<body>
<svg class="sticker" viewBox="0 0 1060 1200" xmlns="http://www.w3.org/2000/svg" role="img" aria-label="Kestrel Vane Labs holographic identification sticker">
  <defs>
    <linearGradient id="holo-frame" x1="0" y1="0" x2="1" y2="1">
      <stop offset="0" stop-color="var(--holo-blue)"/>
      <stop offset="0.18" stop-color="var(--holo-green)"/>
      <stop offset="0.35" stop-color="var(--holo-violet)"/>
      <stop offset="0.5" stop-color="var(--holo-pink)"/>
      <stop offset="0.68" stop-color="var(--holo-blue)"/>
      <stop offset="0.85" stop-color="var(--holo-mint)"/>
      <stop offset="1" stop-color="var(--holo-yellow)"/>
    </linearGradient>
    <linearGradient id="holo-text" x1="0" y1="0" x2="1" y2="0">
      <stop offset="0" stop-color="var(--holo-pink)"/>
      <stop offset="0.3" stop-color="var(--holo-violet)"/>
      <stop offset="0.6" stop-color="var(--holo-pink)"/>
      <stop offset="1" stop-color="var(--holo-mint)"/>
    </linearGradient>
    <linearGradient id="holo-services" x1="0" y1="0" x2="1" y2="0">
      <stop offset="0" stop-color="var(--holo-mint)"/>
      <stop offset="0.4" stop-color="#d8c6ea"/>
      <stop offset="0.7" stop-color="var(--holo-mint)"/>
      <stop offset="1" stop-color="#e4ecd2"/>
    </linearGradient>
  </defs>

  <!-- holographic sticker body -->
  <rect class="frame" x="266" y="213" width="528" height="773" rx="40" fill="url(#holo-frame)"/>

  <!-- main dark panel -->
  <rect class="panel" x="297" y="244" width="465" height="609" rx="18"/>

  <!-- brand mark placeholder -->
  <circle class="brand-circle" cx="530" cy="414" r="140"/>

  <text class="tagline" x="330" y="611" textLength="399" lengthAdjust="spacingAndGlyphs" fill="url(#holo-text)">PROVIDE AVIATION PROFESSIONALS THE FINEST QUALITY</text>

  <text class="company-name" x="330" y="748" font-size="132" textLength="399" lengthAdjust="spacingAndGlyphs">KESTREL</text>
  <text class="company-name" x="330" y="828" font-size="94" textLength="399" lengthAdjust="spacingAndGlyphs">VANE LABS</text>

  <!-- services panel -->
  <rect class="panel" x="297" y="864" width="465" height="90" rx="16"/>
  <text class="services" x="330" y="903" textLength="399" lengthAdjust="spacingAndGlyphs" fill="url(#holo-services)">INSPECTION, REPAIR AND OVERHAULS OF REGIONAL</text>
  <text class="services" x="331" y="928" textLength="398" lengthAdjust="spacingAndGlyphs" fill="url(#holo-services)">AIRCRAFT PROPELLERS AND LARGE PROPELLER SYSTEMS</text>
</svg>
</body>
</html>
```